Italian Dinning Table and wardrobe Selling Website

We need a website design for a reputable furniture company deals in the manufacture of Italian dinning tables and wardrobe. We provide our services to USA based customers.

The categories of the website are
- Home page
- Product page
- The page where all the items are sold
- The shopping cart page

The website is required to have several areas of products with prices that can be added to shopping cart.
Also the website should have customer login facility along with privacy policy, contact us, about us and terms of use
Preferred colors are brown, black and pink,

It Company

```html
<!DOCTYPE html>
<html lang="en">
<head>
<meta charset="utf-8">
<title>Tavolora — Italian Dining Tables</title>
<link href="https://fonts.googleapis.com/css2?family=Jost:wght@300;400;500;600&family=Lora:ital@1&display=swap" rel="stylesheet">
<style>
:root{
  --pink:#df535c;
  --brown:#8a6a4f;
  --ink:#1d1d1d;
  --text:#333;
  --muted:#8d8d8d;
  --line:#d6d6d6;
  --slate:#5c5c5c;
  --white:#fff;
}
*{margin:0;padding:0;box-sizing:border-box}
html,body{width:754px;height:1200px;overflow:hidden;background:var(--white)}
body{font-family:"Jost",sans-serif;color:var(--text);position:relative}
.frame{position:absolute;inset:0;border:5px solid var(--pink);pointer-events:none;z-index:10}
.abs{position:absolute}
.utility{top:11px;left:17px;right:17px;height:12px;font-size:6.5px;color:var(--ink);display:flex;align-items:center}
.utility span{margin-right:14px;display:flex;align-items:center;gap:3px}
.utility .search{margin-left:auto;margin-right:56px;color:#bbb;border-bottom:1px solid #eee;width:120px}
.utility .account{margin:0}
.nav{top:58px;font-size:7px;letter-spacing:.6px;color:#666;font-weight:500}
.nav a{color:inherit;text-decoration:none;margin-right:16px}
.logo{top:46px;left:0;width:754px;text-align:center;font-size:27px;font-weight:300;color:var(--ink);letter-spacing:-.3px}
.hero-photo{left:173px;top:104px;width:531px;height:209px;background:linear-gradient(120deg,#8e8478 0%,#5f554b 35%,#7a5e44 60%,#9a8c7e 100%)}
.deal{left:50px;top:184px;font-family:"Lora",serif;font-style:italic;font-size:9px;color:var(--brown)}
.title-box{left:42px;top:195px;width:321px;height:31px;background:var(--white);padding:4px 0 0 6px;font-size:19px;font-weight:500;color:var(--ink);white-space:nowrap}
.title-box em{font-style:italic;font-weight:600;text-decoration:underline;text-decoration-thickness:1.5px;text-underline-offset:2px}
.desc-box{left:42px;top:231px;width:245px;height:41px;background:var(--white);padding:6px 8px;font-size:7px;line-height:10px;color:var(--ink)}
.from{left:50px;top:277px;font-size:7px;color:var(--ink)}
.price-lead{left:50px;top:287px;font-size:13px;color:var(--ink);font-weight:300}
.btn{display:flex;align-items:center;justify-content:center;color:var(--white);font-size:6.5px;letter-spacing:1.4px;font-weight:600}
.discover{left:50px;top:317px;width:111px;height:21px;background:var(--brown)}
.band{left:50px;top:365px;width:654px;height:167px;background:var(--pink)}
.band-head{left:50px;top:401px;width:654px;text-align:center;color:var(--white);font-size:17px;font-weight:500}
.band-copy{left:210px;top:431px;width:334px;text-align:center;color:var(--white);font-size:7px;line-height:10px}
.cat{width:128px;background:var(--white);text-align:center}
.cat .pic{height:42px;margin:13px 12px 0;background:linear-gradient(#eeeeee,#d9d9d9)}
.cat h3{font-size:6.5px;font-weight:400;letter-spacing:.4px;color:var(--ink);margin-top:22px}
.cat p{font-size:6.5px;line-height:9px;color:var(--ink);margin:4px 14px 0}
.store{left:322px;top:633px;width:110px;height:20px;background:var(--slate)}
.filter{top:679px;height:20px;border:1px solid var(--line);font-size:6.5px;color:#9a9a9a;padding:0 8px;display:flex;align-items:center;justify-content:space-between}
.view{left:675px;top:681px}
.card{width:158px}
.card .photo{height:157px}
.card .label{position:absolute;left:0;top:127px;width:145px;height:30px;background:var(--white);padding:9px 0 0 1px;font-size:9px;font-weight:500;color:var(--ink);white-space:nowrap}
.card .blurb{font-size:6.5px;color:var(--ink);position:absolute;top:157px;white-space:nowrap}
.card .cost{position:absolute;top:170px;font-size:10.5px;font-weight:300;color:var(--ink)}
.p1{background:linear-gradient(160deg,#4b5a3e,#2f2f2c 55%,#9b7a58)}
.p2{background:linear-gradient(170deg,#e4e4e2,#cfcfcc 60%,#a9917a)}
.p3{background:linear-gradient(170deg,#b5b3ae,#8f8c86 55%,#d7d4ce)}
.p4{background:linear-gradient(170deg,#c9c7c3,#9a958e 55%,#6e5a47)}
.loading{left:0;width:754px;top:1116px;text-align:center;font-size:6.5px;color:#ccc;letter-spacing:.4px;display:flex;justify-content:center;align-items:center;gap:6px}
.footer-rule{left:50px;top:1153px;width:654px;height:1px;background:#e8e8e8}
.footer-links{left:51px;top:1158px;font-size:6.5px;color:var(--ink)}
.footer-links a{color:inherit;text-decoration:none;margin-right:13px}
.footer-logo{left:0;width:754px;top:1155px;text-align:center;font-size:11px;font-weight:300;color:var(--ink)}
.social{top:1160px;right:50px;font-size:6.5px;color:var(--ink);display:flex;gap:14px}
.social span{display:flex;align-items:center;gap:2px}
.dot{width:5px;height:5px;background:var(--ink);display:inline-block}
</style>
</head>
<body>
<div class="frame"></div>

<header>
  <div class="abs utility">
    <span><svg width="7" height="7" viewBox="0 0 10 10"><circle cx="5" cy="5" r="4.2" fill="none" stroke="#555" stroke-width="1.2"/></svg>English</span>
    <span>$ USD</span>
    <span><svg width="8" height="6" viewBox="0 0 10 7"><rect x=".5" y=".5" width="9" height="6" fill="none" stroke="#555"/><path d="M.5 .5 5 4l4.5-3.5" fill="none" stroke="#555"/></svg>Contact</span>
    <span>? Assistance</span>
    <span class="search"><svg width="7" height="7" viewBox="0 0 10 10"><circle cx="4" cy="4" r="3" fill="none" stroke="#999" stroke-width="1.3"/><path d="M6.3 6.3 9 9" stroke="#999" stroke-width="1.3"/></svg>Enter search key</span>
    <span class="account"><svg width="6" height="7" viewBox="0 0 8 9"><circle cx="4" cy="2.5" r="2.2" fill="#555"/><path d="M0 9c0-3 1.8-4 4-4s4 1 4 4z" fill="#555"/></svg>My Account</span>
  </div>
  <nav class="abs nav" style="left:123px"><a>SHOP</a><a>CATALOGUES</a><a>COLLECTIONS</a></nav>
  <div class="abs logo">Tavolora<sup style="font-size:8px">®</sup></div>
  <nav class="abs nav" style="left:509px"><a>STORES</a><a>BRAND</a>
    <svg width="9" height="8" viewBox="0 0 10 9"><path d="M0 .5h2l1.5 5.5h5L10 2H3" fill="none" stroke="#666" stroke-width="1.2"/><circle cx="4" cy="8" r=".9" fill="#666"/><circle cx="8" cy="8" r=".9" fill="#666"/></svg>
  </nav>
</header>

<section class="hero">
  <div class="abs hero-photo" role="img" aria-label="Walnut dining table with central glass insert in a dark styled dining room"></div>
  <div class="abs deal">Deal of the day</div>
  <h1 class="abs title-box">“The Canale table”, by <em>Marco Bellandi</em></h1>
  <p class="abs desc-box">A statement piece of any living space. The fascinating central glass insert runs through the entire length of this truly unique table. The top is available in Canaletto walnut or burned oak.</p>
  <div class="abs from">Starting at</div>
  <div class="abs price-lead">$4,924</div>
  <a class="abs btn discover">DISCOVER</a>
</section>

<section class="categories">
  <div class="abs band" role="img" aria-label="Pink banner with faint sketched furniture pattern"></div>
  <h2 class="abs band-head">For sharing meals &amp; being together</h2>
  <p class="abs band-copy">Neque porro quisquam est qui dolorem ipsum quia dolor sit amet, consectetur, adipisci velit. Lorem ipsum dolor sit amet, consectetur adipiscing elit, sed do eiusmod tempor incididunt ut labore et dolore magna aliqua.</p>
  <div class="abs cat" style="left:105px;top:482px"><div class="pic" role="img" aria-label="Fixed dining table"></div><h3>FIXED TABLES</h3><p>Wall-mounted tables Dining table tops &amp; underframes</p></div>
  <div class="abs cat" style="left:244px;top:494px"><div class="pic" role="img" aria-label="Wall-mounted table"></div><h3>WALL-MOUNTED</h3><p>Wall-mounted tables Dining table tops &amp; underframes</p></div>
  <div class="abs cat" style="left:383px;top:482px"><div class="pic" role="img" aria-label="Table top on underframe"></div><h3>TOPS &amp; UNDERFRAMES</h3><p>Wall-mounted tables Dining table tops &amp; underframes</p></div>
  <div class="abs cat" style="left:521px;top:494px"><div class="pic" role="img" aria-label="Extendable table"></div><h3>EXTENDABLE TABLES</h3><p>Wall-mounted tables Dining table tops &amp; underframes</p></div>
  <a class="abs btn store">GO TO STORE</a>
</section>

<section class="catalogue">
  <div class="abs filter" style="left:50px;width:97px">Material<span>⌄</span></div>
  <div class="abs filter" style="left:151px;width:96px">Size<span>⌄</span></div>
  <div class="abs filter" style="left:251px;width:97px">Type<span>⌄</span></div>
  <div class="abs filter" style="left:352px;width:96px">In Stock<span>⌄</span></div>
  <svg class="abs view" width="31" height="15" viewBox="0 0 31 15"><rect x="0" y="2" width="14" height="5" fill="#eee"/><rect x="0" y="9" width="14" height="5" fill="#eee"/><rect x="16" y="0" width="7" height="7" fill="#ccc"/><rect x="24" y="0" width="7" height="7" fill="#ccc"/><rect x="16" y="8" width="7" height="7" fill="#ccc"/><rect x="24" y="8" width="7" height="7" fill="#ccc"/></svg>

  <article class="abs card" style="left:50px;top:709px"><div class="photo p1" role="img" aria-label="Wooden table on glass legs by a large window"></div><h4 class="label">Contemporary ‘Lumen’ glass</h4><p class="blurb">Neque porro quisquam est qui dolorem ipsum</p><div class="cost">$1,614</div></article>
  <article class="abs card" style="left:217px;top:709px"><div class="photo p2" role="img" aria-label="Glass table with blue chair against white brick"></div><h4 class="label">Modern Fixed ‘Orbita’</h4><p class="blurb">Neque porro quisquam est qui dolorem ipsum</p><div class="cost">$987</div></article>
  <article class="abs card" style="left:383px;top:709px"><div class="photo p3" role="img" aria-label="White vintage extending table with slipcovered chairs"></div><h4 class="label">‘Shabby chic’ Extending vintage</h4><p class="blurb">Neque porro quisquam est qui dolorem ipsum</p><div class="cost">$2,764</div></article>
  <article class="abs card" style="left:546px;top:709px"><div class="photo p4" role="img" aria-label="Glass-top table on stone bases under pendant lights"></div><h4 class="label">Fossil stone with glass ‘Corsi’</h4><p class="blurb">Neque porro quisquam est qui dolorem ipsum</p><div class="cost">$1,952</div></article>

  <article class="abs card" style="left:50px;top:908px"><div class="photo p1" role="img" aria-label="Wooden table on glass legs by a large window"></div><h4 class="label">Contemporary ‘Lumen’ glass</h4><p class="blurb">Neque porro quisquam est qui dolorem ipsum</p><div class="cost">$1,614</div></article>
  <article class="abs card" style="left:217px;top:908px"><div class="photo p2" role="img" aria-label="Glass table with blue chair against white brick"></div><h4 class="label">Modern Fixed ‘Orbita’</h4><p class="blurb">Neque porro quisquam est qui dolorem ipsum</p><div class="cost">$987</div></article>
  <article class="abs card" style="left:383px;top:908px"><div class="photo p3" role="img" aria-label="White vintage extending table with slipcovered chairs"></div><h4 class="label">‘Shabby chic’ Extending vintage</h4><p class="blurb">Neque porro quisquam est qui dolorem ipsum</p><div class="cost">$2,764</div></article>
  <article class="abs card" style="left:546px;top:908px"><div class="photo p4" role="img" aria-label="Glass-top table on stone bases under pendant lights"></div><h4 class="label">Fossil stone with glass ‘Corsi’</h4><p class="blurb">Neque porro quisquam est qui dolorem ipsum</p><div class="cost">$1,952</div></article>

  <div class="abs loading"><svg width="12" height="12" viewBox="0 0 12 12"><circle cx="6" cy="6" r="4.6" fill="none" stroke="#ddd" stroke-width="1.6"/><path d="M6 1.4A4.6 4.6 0 0 1 10.6 6" fill="none" stroke="#aaa" stroke-width="1.6"/></svg>LOADING MORE ITEMS</div>
</section>

<footer>
  <div class="abs footer-rule"></div>
  <nav class="abs footer-links"><a>Contact</a><a>Privacy</a><a>General Conditions</a><a>Disclaimer</a></nav>
  <div class="abs footer-logo">Tavolora<sup style="font-size:5px">®</sup></div>
  <div class="abs social"><span><i class="dot"></i>facenet</span><span><i class="dot"></i>chirper</span><span><i class="dot"></i>snapgram</span><span><i class="dot"></i>pinboard</span></div>
</footer>
</body>
</html>
```